Logo and Double sided business card

We need a logo and business card for a Point of Sale Business, Website is www.tillcrest.com.au - this is being worked on at the moment. There is a logo on the website - but this is more of a placement /logo and needs to be redesigned.
The address for Details for the Business card are

Person Name
TILL CREST
27/3 Worrin St
Castle Hill 2154
Ph 1300 482 519 (1300 TIL 519)
Email : Person@tillcrest.com.au
Web: www.tillcrest.com.au

Our company will be a Point of Sale installation and Support business. We Specialise in the Quandel Tivra system.

We do
Installation of POS Systems
Support and Maintenance of existing POS
Tivra POS support
Updates

Target Market(s)

Restaurants, hotels, retail shops

Industry/Entity Type

Business

Contact Information for Business Card

Person Name
TILL CREST
27/3 Worrin St
Castle Hill 2154
Web: www.tillcrest.com.au

Logo Text

Till Crest

Font styles to use
Serif

Requirements
Must have
• We must have the source graphics in editable formats for both logo and business card.

```html
<!DOCTYPE html>
<html lang="en">
<head>
<meta charset="utf-8">
<title>Till Crest business card</title>
<link rel="stylesheet" href="https://fonts.googleapis.com/css2?family=Source+Serif+4:opsz,wght@8..60,400;8..60,600&display=swap">
<style>
  :root {
    --backdrop: #e9e4dc;
    --card-white: #ffffff;
    --amber-deep: #e38a1e;
    --amber-mid: #eda536;
    --amber-light: #f0c45a;
    --gold: #d9a93a;
    --ink: #1d1a16;
    --card-shadow: rgba(60, 40, 10, 0.22);
  }
  * { margin: 0; padding: 0; box-sizing: border-box; }
  html, body {
    width: 1200px; height: 858px; overflow: hidden;
    background: var(--backdrop);
    font-family: "Source Serif 4", serif;
  }
  .sheet {
    position: relative; width: 1200px; height: 858px;
    display: flex; align-items: center; justify-content: center; gap: 40px;
  }
  .card {
    position: relative; width: 540px; height: 330px;
    background: var(--card-white);
    box-shadow: 0 10px 28px var(--card-shadow);
    overflow: hidden;
  }
  .card--front { display: flex; }
  .contact-panel {
    width: 272px; height: 100%; flex: none;
    background: linear-gradient(135deg, var(--amber-deep) 0%, var(--amber-mid) 50%, var(--amber-light) 100%);
    padding: 44px 16px 0 26px;
    color: var(--ink);
    border-right: 6px solid var(--amber-light);
  }
  .person-name { font-size: 26px; font-weight: 400; letter-spacing: 0.2px; }
  .contact-list { list-style: none; margin-top: 74px; font-size: 12.5px; line-height: 1.6; }
  .contact-list li { display: flex; align-items: center; gap: 8px; white-space: nowrap; }
  .contact-list svg { width: 11px; height: 11px; flex: none; fill: var(--ink); }
  .brand-panel {
    flex: 1; display: flex; align-items: center; justify-content: center;
  }
  .brand { display: flex; align-items: center; gap: 12px; color: var(--gold); font-weight: 400; }
  .brand-square { background: var(--gold); flex: none; }
  .brand--small .brand-square { width: 26px; height: 26px; }
  .brand--small .brand-name { font-size: 34px; }
  .card--back { display: flex; align-items: center; justify-content: center; }
  .brand--large .brand-square { width: 40px; height: 40px; }
  .brand--large .brand-name { font-size: 50px; }
</style>
</head>
<body>
<main class="sheet">
  <section class="card card--front" aria-label="Business card front">
    <div class="contact-panel">
      <h1 class="person-name">John Smith</h1>
      <ul class="contact-list">
        <li><svg viewBox="0 0 24 24" aria-hidden="true"><path d="M12 2a7 7 0 0 0-7 7c0 5 7 13 7 13s7-8 7-13a7 7 0 0 0-7-7zm0 9.5A2.5 2.5 0 1 1 12 6.5a2.5 2.5 0 0 1 0 5z"/></svg>27/3 Worrin St, Castle Hill 2154</li>
        <li><svg viewBox="0 0 24 24" aria-hidden="true"><path d="M6.6 10.8a15 15 0 0 0 6.6 6.6l2.2-2.2a1 1 0 0 1 1-.25 11.4 11.4 0 0 0 3.6.57 1 1 0 0 1 1 1V20a1 1 0 0 1-1 1A17 17 0 0 1 3 4a1 1 0 0 1 1-1h3.5a1 1 0 0 1 1 1c0 1.25.2 2.45.57 3.57a1 1 0 0 1-.25 1z"/></svg>1300 482 519 (1300 TIL 519)</li>
        <li><svg viewBox="0 0 24 24" aria-hidden="true"><path d="M2 5h20v14H2z M2 5l10 8 10-8" fill="none" stroke="#1d1a16" stroke-width="2.4"/></svg>Person@tillcrest.com.au</li>
        <li><svg viewBox="0 0 24 24" aria-hidden="true"><circle cx="12" cy="12" r="10" fill="none" stroke="#1d1a16" stroke-width="2.4"/><path d="M2 12h20M12 2c3 3 3 17 0 20M12 2c-3 3-3 17 0 20" fill="none" stroke="#1d1a16" stroke-width="1.8"/></svg>www.tillcrest.com.au</li>
      </ul>
    </div>
    <div class="brand-panel">
      <div class="brand brand--small">
        <span class="brand-square" aria-hidden="true"></span>
        <span class="brand-name">Till Crest</span>
      </div>
    </div>
  </section>
  <section class="card card--back" aria-label="Business card back">
    <div class="brand brand--large">
      <span class="brand-square" aria-hidden="true"></span>
      <span class="brand-name">Till Crest</span>
    </div>
  </section>
</main>
</body>
</html>
```